I need a two page flyer (one page front and back) outlining our residential furniture rental options.

Title: Premium Residential Furniture Rentals

GOOD
Our Brimwell Orla Furniture Package is designed to offer a perfect balance of affordability and style, without compromising on quality. This package features a selection of functional and aesthetically pleasing furniture pieces, ideal for those looking to create a polished and professional space. With quick installation handled by our experienced in-house team, you can expect a smooth and hassle-free setup. This package ensures both convenience and value, providing a streamlined solution for your needs.
Living room, dining room and bedroom (additional bedrooms available)
- $710/month with a 3 month commitment
- $570/month with a 6 month commitment

BETTER
Our Premium Furniture Package takes comfort and style to the next level, offering an enhanced experience compared to our Orla option. Carefully selected with durability in mind, this package features high-quality, convenient furniture designed for both functionality and aesthetics. Perfect for those seeking a more refined look and superior comfort, it’s ideal for creating a sophisticated and inviting environment. With attention to detail in both design and craftsmanship, the premium package elevates any space, ensuring a higher standard of comfort and style that caters to both employees and clients.
- $1,150/month with a 3 month commitment
- $900/month with a 6 month commitment

BEST
Our Custom Furniture Package offers a tailored experience where you’ll work directly with our expert designer to create the ultimate luxurious and functional space. We include lounging, dining, sleeping and working from home, this package allows you to curate a space that perfectly fits your needs and style. With personalized attention to detail, we ensure every element is designed to provide the highest level of comfort, convenience, and elegance, transforming your space into a sophisticated sanctuary for relaxation and enjoyment.
Please inquire for pricing

www.quilbyhomeleasing.com

```html
<!DOCTYPE html>
<html lang="en">
<head>
<meta charset="utf-8">
<title>Quilby Home Leasing – Residential Furniture Rentals</title>
<link href="https://fonts.googleapis.com/css2?family=Montserrat:wght@300;400;500;600;700;800&family=Poppins:wght@600;700&display=swap" rel="stylesheet">
<style>
  :root{
    --navy:#262a6b;
    --ink:#0e0f14;
    --text:#2b2d3a;
    --paper:#f6f6f8;
    --backdrop:#c8cacf;
    --white:#ffffff;
  }
  *{margin:0;padding:0;box-sizing:border-box}
  html,body{width:1200px;height:777px;overflow:hidden}
  body{background:var(--backdrop);font-family:'Montserrat',sans-serif;color:var(--text);position:relative}

  .page{position:absolute;top:47px;width:524px;height:678px;background:var(--paper);overflow:hidden}
  .page--front{left:57px}
  .page--back{left:626px}
  .abs{position:absolute}

  .photo{position:absolute}
  .photo--hero{left:14px;top:13px;width:497px;height:302px;background:linear-gradient(120deg,#9c8a74 0%,#d9d6d0 35%,#ecebe8 60%,#c9c6c0 100%)}
  .photo--bedset{left:34px;top:411px;width:189px;height:96px;background:linear-gradient(90deg,#e9e9ea,#5f6066 40%,#7b7a7c 70%,#e6e6e6)}
  .photo--living{left:38px;top:77px;width:185px;height:213px;background:linear-gradient(160deg,#d7d4cd 0%,#cfc6b4 45%,#5b5a58 80%,#2f3033 100%)}
  .photo--lounge{left:38px;top:393px;width:461px;height:127px;background:linear-gradient(90deg,#6b5b45 0%,#e8ddc4 30%,#b8ab93 55%,#9e9c95 80%,#566b4e 100%)}

  .brand-box{left:190px;top:13px;width:142px;height:95px;background:var(--white);display:flex;flex-direction:column;align-items:center;justify-content:center;gap:6px}
  .brand-square{width:22px;height:22px;border:2px solid var(--navy)}
  .brand-name{font-weight:500;font-size:10.5px;letter-spacing:.4px;color:var(--navy);text-align:center;line-height:1.25}

  .title-panel{left:50px;top:260px;width:427px;height:94px;background:var(--ink);color:var(--white);font-weight:800;font-size:26px;line-height:33px;text-align:center;display:flex;align-items:center;justify-content:center;letter-spacing:.3px}

  .tier-head{display:flex;align-items:flex-end;gap:5px;color:var(--navy);font-weight:800;font-size:22px;line-height:1}
  .tier-head::after{content:"";flex:1;height:1.2px;background:var(--navy);margin-bottom:4px}

  .copy{font-weight:400;font-size:9.4px;line-height:11.3px;color:var(--text)}

  .price{position:absolute;width:72px;height:68px;background:var(--navy);color:var(--white);text-align:center;padding-top:9px}
  .price-amt{font-family:'Poppins',sans-serif;font-weight:700;font-size:22px;line-height:22px}
  .price-amt sup{font-size:10px;vertical-align:top;line-height:12px}
  .price-tag{display:inline-block;background:var(--ink);font-weight:700;font-size:7px;padding:1px 4px;margin-top:2px}
  .price-term{font-size:6.2px;line-height:7px;margin-top:3px;font-weight:400}

  .room{position:absolute;width:90px;margin-left:-45px;text-align:center}
  .room svg{display:block;margin:0 auto}
  .room-label{font-size:9.5px;margin-top:7px;color:var(--text)}
  .room-sep{position:absolute;width:0;height:52px;border-left:1px dotted #8a8ca0}
  .extra-note{font-size:8px;font-style:italic;color:#d9d9df;text-align:center}

  .brand-line{left:315px;top:302px;display:flex;align-items:center;gap:7px}
  .brand-line .brand-square{width:26px;height:26px}
  .brand-line .brand-name{font-size:12.5px;text-align:left}

  .inquire{left:0;width:524px;top:609px;text-align:center;font-weight:700;font-size:11px;color:var(--navy)}

  .footer{left:0;width:524px;height:43px;background:var(--ink);color:var(--white);font-weight:400;font-size:13.5px;display:flex;align-items:center;justify-content:center;letter-spacing:.2px}
</style>
</head>
<body>

<section class="page page--front">
  <div class="photo photo--hero" role="img" aria-label="Furnished apartment with kitchen, bedroom and living area"></div>
  <div class="abs brand-box">
    <div class="brand-square"></div>
    <div class="brand-name">QUILBY HOME LEASING</div>
  </div>
  <h1 class="abs title-panel">PREMIUM RESIDENTIAL<br>FURNITURE RENTALS</h1>

  <h2 class="abs tier-head" style="left:39px;top:376px;width:458px">GOOD</h2>
  <div class="photo photo--bedset" role="img" aria-label="Bedroom set with tufted bed, nightstand and dresser"></div>
  <p class="abs copy" style="left:240px;top:410px;width:258px">Our Brimwell Orla Furniture Package is designed to offer a perfect balance of affordability and style, without compromising on quality. This package features a selection of functional and aesthetically pleasing furniture pieces, ideal for those looking to create a polished and professional space. With quick installation handled by our experienced in-house team, you can expect a smooth and hassle-free setup. This package ensures both convenience and value, providing a streamlined solution for your needs.</p>

  <div class="price" style="left:45px;top:525px">
    <div class="price-amt"><sup>$</sup>710</div>
    <div class="price-tag">PER MONTH</div>
    <div class="price-term">with a 3 month<br>commitment</div>
  </div>
  <div class="price" style="left:121px;top:525px">
    <div class="price-amt"><sup>$</sup>570</div>
    <div class="price-tag">PER MONTH</div>
    <div class="price-term">with a 6 month<br>commitment</div>
  </div>

  <div class="room" style="left:266px;top:532px">
    <svg width="40" height="40" viewBox="0 0 40 40" fill="none" stroke="#262a6b" stroke-width="1.2"><circle cx="20" cy="20" r="19"/><path d="M10 26h20M12 26v-6h16v6M14 20v-3h12v3M13 26v2M27 26v2"/><path d="M11 14h4M13 14v6"/></svg>
    <div class="room-label">Living room</div>
  </div>
  <div class="room-sep" style="left:310px;top:536px"></div>
  <div class="room" style="left:355px;top:532px">
    <svg width="40" height="40" viewBox="0 0 40 40" fill="none" stroke="#262a6b" stroke-width="1.2"><circle cx="20" cy="20" r="19"/><rect x="14" y="9" width="12" height="7"/><path d="M12 21h16M15 21v8M25 21v8M10 17v12M10 23h4M30 17v12M30 23h-4"/></svg>
    <div class="room-label">dining room and</div>
  </div>
  <div class="room-sep" style="left:404px;top:536px"></div>
  <div class="room" style="left:440px;top:532px">
    <svg width="40" height="40" viewBox="0 0 40 40" fill="none" stroke="#262a6b" stroke-width="1.2"><circle cx="20" cy="20" r="19"/><rect x="14" y="9" width="12" height="6"/><path d="M10 20h20v6H10zM10 26v3M30 26v3M12 20v-3h7v3M21 20v-3h7v3"/></svg>
    <div class="room-label">bedroom</div>
  </div>
  <div class="abs extra-note" style="left:240px;top:585px;width:258px">(additional bedrooms available)</div>

  <div class="abs footer" style="top:634px">www.quilbyhomeleasing.com</div>
</section>

<section class="page page--back">
  <h2 class="abs tier-head" style="left:39px;top:37px;width:459px">BETTER</h2>
  <div class="photo photo--living" role="img" aria-label="Living room with beige sofa, armchair and abstract wall art"></div>
  <div class="price" style="left:59px;top:258px">
    <div class="price-amt"><sup>$</sup>1150</div>
    <div class="price-tag">PER MONTH</div>
    <div class="price-term">with a 3 month<br>commitment</div>
  </div>
  <div class="price" style="left:135px;top:258px">
    <div class="price-amt"><sup>$</sup>900</div>
    <div class="price-tag">PER MONTH</div>
    <div class="price-term">with a 6 month<br>commitment</div>
  </div>
  <p class="abs copy" style="left:243px;top:76px;width:256px">Our Premium Furniture Package takes comfort and style to the next level, offering an enhanced experience compared to our Orla option. Carefully selected with durability in mind, this package features high-quality, convenient furniture designed for both functionality and aesthetics. Perfect for those seeking a more refined look and superior comfort, it’s ideal for creating a sophisticated and inviting environment. With attention to detail in both design and craftsmanship, the premium package elevates any space, ensuring a higher standard of comfort and style that caters to both employees and clients.</p>

  <div class="room" style="left:269px;top:216px">
    <svg width="40" height="40" viewBox="0 0 40 40" fill="none" stroke="#262a6b" stroke-width="1.2"><circle cx="20" cy="20" r="19"/><path d="M10 26h20M12 26v-6h16v6M14 20v-3h12v3M13 26v2M27 26v2"/><path d="M11 14h4M13 14v6"/></svg>
    <div class="room-label">Living room</div>
  </div>
  <div class="room-sep" style="left:312px;top:220px"></div>
  <div class="room" style="left:358px;top:216px">
    <svg width="40" height="40" viewBox="0 0 40 40" fill="none" stroke="#262a6b" stroke-width="1.2"><circle cx="20" cy="20" r="19"/><rect x="14" y="9" width="12" height="7"/><path d="M12 21h16M15 21v8M25 21v8M10 17v12M10 23h4M30 17v12M30 23h-4"/></svg>
    <div class="room-label">dining room and</div>
  </div>
  <div class="room-sep" style="left:408px;top:220px"></div>
  <div class="room" style="left:443px;top:216px">
    <svg width="40" height="40" viewBox="0 0 40 40" fill="none" stroke="#262a6b" stroke-width="1.2"><circle cx="20" cy="20" r="19"/><rect x="14" y="9" width="12" height="6"/><path d="M10 20h20v6H10zM10 26v3M30 26v3M12 20v-3h7v3M21 20v-3h7v3"/></svg>
    <div class="room-label">bedroom</div>
  </div>
  <div class="abs extra-note" style="left:243px;top:281px;width:256px">(additional bedrooms available)</div>

  <div class="abs brand-line">
    <div class="brand-square"></div>
    <div class="brand-name">QUILBY HOME LEASING</div>
  </div>

  <h2 class="abs tier-head" style="left:39px;top:352px;width:459px">BEST</h2>
  <div class="photo photo--lounge" role="img" aria-label="Bright lounge with sectional sofa, navy armchairs and fireplace"></div>
  <p class="abs copy" style="left:40px;top:530px;width:460px">Our Custom Furniture Package offers a tailored experience where you’ll work directly with our expert designer to create the ultimate luxurious and functional space. We include lounging, dining, sleeping and working from home, this package allows you to curate a space that perfectly fits your needs and style. With personalized attention to detail, we ensure every element is designed to provide the highest level of comfort, convenience, and elegance, transforming your space into a sophisticated sanctuary for relaxation and enjoyment.</p>
  <p class="abs inquire">Please inquire for pricing</p>

  <div class="abs footer" style="top:636px">www.quilbyhomeleasing.com</div>
</section>

</body>
</html>
```